Concession stand banners for a mexican food tent

I'm looking for a clean easy to read design for a set of banners I need. More info is on the pic I uploaded. Simple modern design with just text.must say taco,burrito,burrito bowl,salad and nachos. I looking for a dark color(black or brown with colored text. I attached a picture what the setup will look like and where the banners are located.

Target Market(s)

food industry ,food truck, food tent

Font styles to use
Sans Serif

Requirements
Must have
• Must say tacos, burritos, burrito bowls, salads,nachos
Nice to have
• Easy to read from a distance.
Should not have
• hard to read text

```html
<!DOCTYPE html>
<html lang="en">
<head>
<meta charset="utf-8">
<title>Concession Stand Banners</title>
<link href="https://fonts.googleapis.com/css2?family=Rye&display=swap" rel="stylesheet">
<style>
  :root {
    --page: #ffffff;
    --banner: #000000;
    --yellow: #ffe600;
    --orange: #ff8a00;
    --red-orange: #ff5a00;
    --red: #d40000;
    --green: #00ff00;
    --magenta: #ff00e6;
  }
  * { box-sizing: border-box; margin: 0; padding: 0; }
  html, body {
    width: 1200px;
    height: 968px;
    overflow: hidden;
    background: var(--page);
  }
  .sheet {
    position: relative;
    width: 1200px;
    height: 968px;
  }
  .banner {
    position: absolute;
    width: 524px;
    height: 259px;
    background: var(--banner);
    display: flex;
    align-items: center;
    justify-content: center;
    overflow: hidden;
  }
  .banner--tacos   { left: 63px;  top: 57px; }
  .banner--nachos  { left: 613px; top: 57px; }
  .banner--burritos{ left: 63px;  top: 350px; }
  .banner--salads  { left: 613px; top: 350px; }
  .banner--bowls   { left: 338px; top: 651px; }

  .border-band {
    position: absolute;
    left: 0;
    width: 100%;
  }
  .border-band--top    { top: 8px; }
  .border-band--bottom { bottom: 8px; }

  .banner--tacos .border-band {
    height: 22px;
    background: linear-gradient(180deg, var(--yellow) 0%, var(--red-orange) 100%);
  }
  .banner--tacos .border-band--bottom {
    background: linear-gradient(180deg, var(--red-orange) 0%, var(--yellow) 100%);
  }
  .banner--nachos .border-band { height: 22px; background: var(--magenta); }
  .banner--burritos .border-band { height: 28px; background: #8a7a00; }
  .banner--burritos .border-band--top { top: 0; }
  .banner--burritos .border-band--bottom { bottom: 0; }
  .banner--salads .border-band { height: 26px; background: var(--green); }
  .banner--bowls .border-band { height: 18px; background: #b34000; }

  .label {
    font-family: "Rye", "Georgia", serif;
    text-transform: uppercase;
    text-align: center;
    line-height: 1;
    letter-spacing: 0.04em;
    white-space: nowrap;
  }
  .label--tacos {
    font-size: 88px;
    color: var(--yellow);
    text-shadow: -4px -3px 0 var(--red-orange);
  }
  .label--nachos {
    font-size: 66px;
    color: var(--green);
    margin-top: -16px;
  }
  .label--burritos {
    font-size: 52px;
    color: var(--red);
    margin-top: -8px;
  }
  .label--salads {
    font-size: 76px;
    color: var(--orange);
    margin-top: -20px;
  }
  .label--bowls {
    font-size: 64px;
    color: var(--magenta);
    line-height: 1.08;
  }
</style>
</head>
<body>
  <main class="sheet">
    <section class="banner banner--tacos">
      <div class="border-band border-band--top" role="img" aria-label="Yellow and orange zigzag border"></div>
      <h2 class="label label--tacos">Tacos</h2>
      <div class="border-band border-band--bottom" role="img" aria-label="Orange and yellow zigzag border"></div>
    </section>

    <section class="banner banner--nachos">
      <div class="border-band border-band--top" role="img" aria-label="Magenta diamond chain border"></div>
      <h2 class="label label--nachos">Nachos</h2>
      <div class="border-band border-band--bottom" role="img" aria-label="Magenta diamond chain border"></div>
    </section>

    <section class="banner banner--burritos">
      <div class="border-band border-band--top" role="img" aria-label="Yellow chevron line border"></div>
      <h2 class="label label--burritos">Burritos</h2>
      <div class="border-band border-band--bottom" role="img" aria-label="Yellow chevron line border"></div>
    </section>

    <section class="banner banner--salads">
      <div class="border-band border-band--top" role="img" aria-label="Green diamond chain border"></div>
      <h2 class="label label--salads">Salads</h2>
      <div class="border-band border-band--bottom" role="img" aria-label="Green diamond chain border"></div>
    </section>

    <section class="banner banner--bowls">
      <div class="border-band border-band--top" role="img" aria-label="Orange outlined diamond border"></div>
      <h2 class="label label--bowls">Burrito<br>Bowls</h2>
      <div class="border-band border-band--bottom" role="img" aria-label="Orange outlined diamond border"></div>
    </section>
  </main>
</body>
</html>
```